Business Card Design for Varnor Facility Services

We are looking for a Business Card Design for the Company "Varnor Facility Services."
Front side:
- Company Logo (small)
- Company Name, address, pohone, website and personal data.
- white background, for text e.g. company colors (blue or green like in the logo)
Please use following data:
Company data:
Varnor Facility Services Kuttelbrand
Lindauweg 14
6347 Brunnfeld
www.varnor-fs.example
Person data:
Tobias Kuttelbrand
Geschäftsführer
+41 76 915 47 18
info@varnor-fs.example
Back side:
could be colored in blue or green
please use a big logo sing and some smaller icons to say what is all beeing offered in facility services, like cleaning, maintenance cleaning
industrial cleaning, caretaking, gardening, disposal. There is no need for everyone of the icons if there are similar or an icon is standing for more of them.
Cleaning Service
colors to use:
blue: HEX 246BB0
green: HEX 52B33E

```html
<!DOCTYPE html>
<html lang="de">
<head>
<meta charset="utf-8">
<title>Varnor Facility Services – Visitenkarte</title>
<link href="https://fonts.googleapis.com/css2?family=Source+Sans+3:wght@400;600&display=swap" rel="stylesheet">
<style>
  :root {
    --brand-blue: #1569b3;
    --brand-green: #5ab946;
    --paper: #ffffff;
    --canvas: #ffffff;
    --ink-light: #ffffff;
  }
  * { margin: 0; padding: 0; box-sizing: border-box; }
  html, body {
    width: 1200px; height: 960px; overflow: hidden;
    background: var(--canvas);
    font-family: "Source Sans 3", "Source Sans Pro", sans-serif;
  }
  .card {
    position: absolute; left: 286px; width: 629px; height: 359px;
    background: var(--paper);
    box-shadow: 0 1px 5px rgba(0,0,0,0.28);
    overflow: hidden;
  }
  .card--front { top: 109px; }
  .card--back { top: 492px; }
  .card__panel {
    position: absolute; left: 336px; top: 0; right: 0; bottom: 0;
    background: var(--brand-blue);
  }
  .card__stripe {
    position: absolute; left: 0; right: 0; height: 11px;
    background: var(--brand-green);
  }
  .card__stripe--upper { top: 335px; }
  .card__stripe--lower { top: 349px; height: 10px; }
  .brand {
    position: absolute; left: 0; width: 336px; top: 160px;
    display: flex; align-items: center; justify-content: center; gap: 9px;
  }
  .brand__dot {
    width: 14px; height: 14px; border-radius: 50%;
    background: var(--brand-green); flex: none;
  }
  .brand__name {
    font-size: 22px; font-weight: 600; color: var(--brand-blue);
    letter-spacing: 0.5px; white-space: nowrap;
  }
  .details {
    position: absolute; left: 381px; top: 0;
    color: var(--ink-light);
  }
  .details__name {
    position: absolute; top: 70px; font-size: 24px; font-weight: 600; white-space: nowrap;
  }
  .details__role {
    position: absolute; top: 101px; font-size: 19px; white-space: nowrap;
  }
  .details__address {
    position: absolute; top: 150px; font-size: 17px; line-height: 26.5px; white-space: nowrap;
  }
  .contact {
    position: absolute; top: 209px; list-style: none; font-size: 17px;
  }
  .contact li {
    height: 26.5px; display: flex; align-items: center; white-space: nowrap;
  }
  .contact svg { width: 16px; height: 16px; margin-right: 15px; flex: none; }
  .services {
    position: absolute; left: 385px; top: 101px; list-style: none;
    color: var(--ink-light); font-size: 17.5px;
  }
  .services li {
    height: 26.4px; display: flex; align-items: center; white-space: nowrap;
  }
  .services svg { width: 16px; height: 16px; margin-right: 13px; flex: none; }
</style>
</head>
<body>

<section class="card card--front" aria-label="Vorderseite">
  <div class="brand">
    <span class="brand__dot"></span>
    <span class="brand__name">Varnor Facility Services</span>
  </div>
  <div class="card__panel"></div>
  <div class="details">
    <p class="details__name">Tobias Kuttelbrand</p>
    <p class="details__role">Geschäftsführer</p>
    <p class="details__address">Lindauweg 14<br>6347 Brunnfeld</p>
    <ul class="contact">
      <li>
        <svg viewBox="0 0 16 16" aria-hidden="true"><path fill="#fff" d="M3.2 1.2l2.3 2.6-1.2 1.6c.9 2 2.4 3.6 4.4 4.6l1.6-1.2 2.6 2.3-1.5 2.3C6.6 13.2 2.6 9.2 1 4.2z"/></svg>
        +41 76 915 47 18
      </li>
      <li>
        <svg viewBox="0 0 16 16" aria-hidden="true"><rect x="1" y="3.5" width="14" height="10" fill="#fff"/><path d="M1.5 4l6.5 5 6.5-5M1.5 13l5-4.5M14.5 13l-5-4.5" stroke="var(--brand-blue)" stroke-width="1.2" fill="none"/></svg>
        info@varnor-fs.example
      </li>
      <li>
        <svg viewBox="0 0 16 16" aria-hidden="true"><circle cx="8" cy="8" r="6.6" fill="none" stroke="#fff" stroke-width="1.6"/><path d="M1.6 8h12.8M8 1.4c-2.4 2-2.4 11.2 0 13.2M8 1.4c2.4 2 2.4 11.2 0 13.2" stroke="#fff" stroke-width="1.2" fill="none"/></svg>
        www.varnor-fs.example
      </li>
    </ul>
  </div>
  <div class="card__stripe card__stripe--upper"></div>
  <div class="card__stripe card__stripe--lower"></div>
</section>

<section class="card card--back" aria-label="Rückseite">
  <div class="brand">
    <span class="brand__dot"></span>
    <span class="brand__name">Varnor Facility Services</span>
  </div>
  <div class="card__panel"></div>
  <ul class="services">
    <li><svg viewBox="0 0 16 16" aria-hidden="true"><path fill="#fff" d="M8 0l1.3 6.7L16 8l-6.7 1.3L8 16l-1.3-6.7L0 8l6.7-1.3z"/></svg>Like cleaning</li>
    <li><svg viewBox="0 0 16 16" aria-hidden="true"><path fill="#fff" d="M8 0l1.3 6.7L16 8l-6.7 1.3L8 16l-1.3-6.7L0 8l6.7-1.3z"/></svg>Maintenance cleaning</li>
    <li><svg viewBox="0 0 16 16" aria-hidden="true"><path fill="#fff" d="M8 0l1.3 6.7L16 8l-6.7 1.3L8 16l-1.3-6.7L0 8l6.7-1.3z"/></svg>Industrial cleaning</li>
    <li><svg viewBox="0 0 16 16" aria-hidden="true"><path fill="#fff" d="M8 0l1.3 6.7L16 8l-6.7 1.3L8 16l-1.3-6.7L0 8l6.7-1.3z"/></svg>Caretaking</li>
    <li><svg viewBox="0 0 16 16" aria-hidden="true"><path fill="#fff" d="M8 0l1.3 6.7L16 8l-6.7 1.3L8 16l-1.3-6.7L0 8l6.7-1.3z"/></svg>Gardening</li>
    <li><svg viewBox="0 0 16 16" aria-hidden="true"><path fill="#fff" d="M8 0l1.3 6.7L16 8l-6.7 1.3L8 16l-1.3-6.7L0 8l6.7-1.3z"/></svg>Disposal</li>
  </ul>
  <div class="card__stripe card__stripe--upper"></div>
  <div class="card__stripe card__stripe--lower"></div>
</section>

</body>
</html>
```